Facebook post - Shine Corner Tiling has arrived to make your tiles smile!

Shine Corner Tiling would like to release a Facebook post calling out to the market that we have arrived. The company has a new and fresh branding aiming for a female demographic between the ages of 40 and 55 located in the South West of Western Australia. The company image MUST be centered around trust! Our Primary aim is to create an uncompromising trust from the very first impression. Our logo tag line is, 'We love to make your tiles smile'.
I need 5 x facebook template designs and also 5 x posts.
Our 1st campaign is to be 5 x posts centered around the arrival of this fantastic new company.
We are company that provides the services of:
- Grout and silicone repair.
- Broken or drummy tile replacement and;
- Grout sealing
Dont forget that we must communicate TRUST and the we love to make your tiles SMILE!

```html
<!DOCTYPE html>
<html lang="en">
<head>
<meta charset="utf-8">
<title>Shine Corner Tiling – Facebook post set</title>
<link rel="stylesheet" href="https://fonts.googleapis.com/css2?family=Teko:wght@400;500;600&family=Saira+Condensed:wght@400;500&family=Lato:wght@400;700&display=swap">
<style>
  :root {
    --blue: #1ba4de;
    --blue-deep: #1590c6;
    --mist: #f3f3f3;
    --white: #ffffff;
    --ink: #1e1e1e;
    --body: #2a2a2a;
    --photo-a: #cfc6bd;
    --photo-b: #8f7a68;
    --photo-c: #e9e7e4;
  }
  * { box-sizing: border-box; margin: 0; padding: 0; }
  html, body { width: 1200px; height: 3051px; overflow: hidden; background: var(--white); }
  .canvas { position: relative; width: 1200px; height: 3051px; }

  .post { position: absolute; left: 75px; width: 1028px; height: 539px; overflow: hidden; background: var(--mist); }
  .post--1 { top: 64px; }
  .post--2 { top: 638px; }
  .post--3 { top: 1220px; background: var(--blue); }
  .post--4 { top: 1806px; }
  .post--5 { top: 2402px; background: var(--blue); }
  .layer { position: absolute; }
  .shape { position: absolute; left: 0; top: 0; width: 1028px; height: 539px; }

  .photo { background: linear-gradient(160deg, var(--photo-b) 0%, var(--photo-a) 38%, var(--photo-c) 70%, #f7f6f4 100%); }
  .van { border-radius: 40px 60px 14px 14px; background: linear-gradient(180deg, #ffffff 0%, #eef2f4 55%, #4fb3dd 80%, #2c2c2c 100%); }

  .brand { position: absolute; display: flex; align-items: center; gap: 12px; white-space: nowrap; }
  .brand__mark { flex: none; width: 34px; height: 34px; border-radius: 50%; background: var(--blue); }
  .brand__name { font-family: "Teko", sans-serif; font-weight: 500; font-size: 30px; letter-spacing: 0.5px; color: var(--blue); line-height: 1; white-space: nowrap; }
  .brand--compact { gap: 9px; }
  .brand--compact .brand__mark { width: 24px; height: 24px; }
  .brand--compact .brand__name { font-size: 22px; }
  .brand--light .brand__mark { background: var(--white); }
  .brand--light .brand__name { color: var(--white); }

  .headline { position: absolute; font-family: "Teko", sans-serif; font-weight: 500; line-height: 0.9; text-transform: uppercase; letter-spacing: 2px; white-space: nowrap; }
  .headline__chip { background: var(--white); color: var(--blue); padding: 0 6px; }
  .headline__light { color: var(--white); }
  .headline__blue { color: var(--blue); }
  .headline__dark { color: var(--ink); }
  .headline--boxed { display: flex; align-items: center; justify-content: center; width: 356px; height: 70px; padding-top: 8px; background: var(--white); font-size: 68px; letter-spacing: 1px; gap: 14px; }
  .subhead { position: absolute; font-family: "Saira Condensed", sans-serif; font-weight: 500; color: var(--white); letter-spacing: 1.5px; white-space: nowrap; }

  .copy { position: absolute; font-family: "Lato", sans-serif; font-size: 19px; line-height: 25px; color: var(--body); }
  .copy--light { color: var(--white); }
  .copy--boxed { background: var(--white); padding: 4px 8px 6px; }

  .callout { position: absolute; background: var(--white); border: 2px solid var(--blue); padding: 10px 14px; font-family: "Saira Condensed", sans-serif; font-size: 23px; line-height: 31px; color: var(--ink); letter-spacing: 0.6px; white-space: nowrap; }
  .callout--plain { border-color: var(--white); }
  .callout strong { color: var(--blue); font-weight: 500; }

  .dots { position: absolute; background-image: radial-gradient(circle, var(--blue) 2.6px, transparent 3px); background-size: 30px 30px; }
  .dots--light { background-image: radial-gradient(circle, var(--white) 2.6px, transparent 3px); }
  .dots--faint { background-image: radial-gradient(circle, rgba(255,255,255,0.35) 4px, transparent 4.5px); background-size: 26px 26px; }

  .services { position: absolute; left: 786px; top: 160px; list-style: none; font-family: "Lato", sans-serif; }
  .services__label { font-size: 13px; color: var(--body); margin: 0 0 18px 18px; letter-spacing: 0.3px; }
  .services__item { border-left: 5px solid var(--blue); padding-left: 14px; font-size: 21px; color: var(--body); height: 28px; line-height: 28px; margin-bottom: 24px; white-space: nowrap; }
</style>
</head>
<body>
<main class="canvas">

  <!-- Post 1: Broken or drummy tile replacement -->
  <section class="post post--1">
    <div class="layer photo" style="left:0;top:0;width:609px;height:539px" role="img" aria-label="Bright bathroom with marble tiles, basin and mirror cabinet"></div>
    <div class="brand" style="left:720px;top:78px"><span class="brand__mark"></span><span class="brand__name">SHINE CORNER TILING</span></div>
    <div class="headline" style="left:348px;top:162px;font-size:60px"><span class="headline__chip">Broken or drummy tile</span></div>
    <div class="subhead" style="left:350px;top:214px;font-size:46px">Replacement</div>
    <p class="copy" style="left:621px;top:268px">Lorem ipsum dolor sit amet,<br>consectetuer adipiscing elit.<br>Aenean commodo ligula eget</p>
    <div class="dots" style="left:940px;top:190px;width:90px;height:150px"></div>
    <div class="layer van" style="left:622px;top:392px;width:406px;height:147px" role="img" aria-label="Branded white service van"></div>
    <p class="callout" style="left:84px;top:391px;width:310px">Dont forget that we must<br>communicate <strong>TRUST</strong> and the we<br>love to make your tiles <strong>SMILE</strong>!</p>
  </section>

  <!-- Post 2: Grout & silicone rejuvenation -->
  <section class="post post--2">
    <svg class="shape" viewBox="0 0 1028 539" aria-hidden="true"><polygon points="0,0 429,0 405,100 165,100 165,539 0,539" fill="var(--blue)"/></svg>
    <div class="layer photo" style="left:165px;top:100px;width:611px;height:439px" role="img" aria-label="Bathroom vanity with marble wall tiles and shelving"></div>
    <div class="dots dots--light" style="left:40px;top:30px;width:120px;height:150px"></div>
    <div class="headline" style="left:204px;top:30px;font-size:78px"><span class="headline__light">Grout &amp; </span><span class="headline__blue">Silicone</span></div>
    <div class="subhead" style="left:204px;top:104px;font-size:40px">Rejuvenation</div>
    <p class="callout callout--plain" style="left:23px;top:183px;width:301px">Dont forget that we must<br>communicate <strong>TRUST</strong> and the we<br>love to make your tiles <strong>SMILE</strong></p>
    <div class="brand brand--compact" style="left:818px;top:106px"><span class="brand__mark"></span><span class="brand__name">SHINE CORNER TILING</span></div>
    <ul class="services">
      <li class="services__label">WHAT WE DO</li>
      <li class="services__item">Grout Repair</li>
      <li class="services__item">Grout Sealing</li>
      <li class="services__item">Silicone Replacement</li>
      <li class="services__item">Obligation Free Quotes</li>
    </ul>
    <div class="layer van" style="left:601px;top:392px;width:422px;height:147px" role="img" aria-label="Branded white service van"></div>
  </section>

  <!-- Post 3: Grout sealing -->
  <section class="post post--3">
    <svg class="shape" viewBox="0 0 1028 539" aria-hidden="true">
      <polygon points="0,368 208,345 208,539 0,539" fill="var(--mist)"/>
      <polygon points="813,222 1028,190 1028,539 813,539" fill="var(--mist)"/>
    </svg>
    <div class="dots dots--faint" style="left:0;top:0;width:300px;height:80px"></div>
    <div class="layer photo" style="left:208px;top:61px;width:605px;height:478px" role="img" aria-label="Bathroom basin and mirror cabinet with marble tiling"></div>
    <div class="headline" style="left:54px;top:110px;font-size:74px"><span class="headline__light">Grout </span><span class="headline__chip">Sealing</span></div>
    <p class="copy copy--light" style="left:45px;top:212px">Lorem ipsum dolor sit amet,<br>consectetuer adipiscing elit.<br>Aenean commodo ligula eget</p>
    <div class="brand brand--light brand--compact" style="left:830px;top:112px"><span class="brand__mark"></span><span class="brand__name">SHINE CORNER TILING</span></div>
    <div class="layer van" style="left:822px;top:303px;width:199px;height:76px" role="img" aria-label="Branded white service van"></div>
    <p class="callout" style="left:704px;top:379px;width:313px">Dont forget that we must<br>communicate <strong>TRUST</strong> and the we<br>love to make your tiles <strong>SMILE!</strong></p>
    <div class="dots" style="left:940px;top:495px;width:90px;height:44px"></div>
  </section>

  <!-- Post 4: Lorem ipsum on light -->
  <section class="post post--4">
    <svg class="shape" viewBox="0 0 1028 539" aria-hidden="true">
      <polygon points="0,40 0,539 330,539 39,300 240,0 110,0" fill="var(--blue)"/>
      <polygon points="570,539 1028,380 1028,539" fill="var(--blue)"/>
    </svg>
    <svg class="shape" viewBox="0 0 1028 539" role="img" aria-label="Bathroom interior with marble tiles and vanity">
      <defs><linearGradient id="room" x1="0" y1="0" x2="0.6" y2="1"><stop offset="0" stop-color="#8f7a68"/><stop offset="0.4" stop-color="#cfc6bd"/><stop offset="1" stop-color="#f1efec"/></linearGradient></defs>
      <polygon points="39,300 260,0 720,0 600,240 800,330 580,539 330,539" fill="url(#room)"/>
    </svg>
    <div class="dots" style="left:105px;top:22px;width:120px;height:60px"></div>
    <div class="brand" style="left:700px;top:78px"><span class="brand__mark"></span><span class="brand__name">SHINE CORNER TILING</span></div>
    <div class="headline headline--boxed" style="left:636px;top:140px"><span class="headline__blue">Lorem</span><span class="headline__dark">Ipsum</span></div>
    <p class="copy copy--boxed" style="left:604px;top:245px;width:392px">Lorem ipsum dolor sit amet, consectetuer adipiscing elit. Aenean commodo ligula eget</p>
    <div class="dots" style="left:985px;top:275px;width:45px;height:120px"></div>
    <div class="layer van" style="left:624px;top:392px;width:404px;height:147px" role="img" aria-label="Branded white service van"></div>
    <p class="callout" style="left:27px;top:392px;width:309px">Dont forget that we must<br>communicate <strong>TRUST</strong> and the we<br>love to make your tiles <strong>SMILE</strong>!</p>
  </section>

  <!-- Post 5: Lorem ipsum on blue -->
  <section class="post post--5">
    <div class="dots dots--light" style="left:0;top:20px;width:70px;height:130px"></div>
    <svg class="shape" viewBox="0 0 1028 539" role="img" aria-label="Bathroom interior with marble tiles and vanity">
      <defs><linearGradient id="room5" x1="0" y1="0" x2="0.6" y2="1"><stop offset="0" stop-color="#8f7a68"/><stop offset="0.4" stop-color="#cfc6bd"/><stop offset="1" stop-color="#f1efec"/></linearGradient></defs>
      <polygon points="165,0 634,0 541,539 36,539" fill="url(#room5)" stroke="var(--white)" stroke-width="5"/>
    </svg>
    <div class="brand brand--light" style="left:700px;top:78px"><span class="brand__mark"></span><span class="brand__name">SHINE CORNER TILING</span></div>
    <div class="headline headline--boxed" style="left:636px;top:138px"><span class="headline__blue">Lorem</span><span class="headline__dark">Ipsum</span></div>
    <p class="copy copy--light" style="left:617px;top:264px;width:390px">Lorem ipsum dolor sit amet, consectetuer adipiscing elit. Aenean commodo ligula eget</p>
    <div class="dots dots--light" style="left:960px;top:365px;width:60px;height:150px"></div>
    <div class="layer van" style="left:540px;top:387px;width:404px;height:150px;border-radius:60px 40px 14px 14px" role="img" aria-label="Branded white service van"></div>
    <p class="callout" style="left:27px;top:390px;width:309px">Dont forget that we must<br>communicate <strong>TRUST</strong> and the we<br>love to make your tiles <strong>SMILE</strong>!</p>
  </section>

</main>
</body>
</html>
```